Chiropractic healthcare group business card

We are a Portland Oregon based chiropractic healthcare group. Looking for a new business card design. Something cutting edge, that shows off our new logo and tag line.Use either of the attached logos.Our tag line = "Who would you be without pain?"I'm open to about anything, impress me!!
Target Market(s)
Chiropractic patients - Auto injury, back pain, sports injuries, neck , shoulder, hip, knee, ankle pain.
Industry/Entity Type
Chiropractic
Contact Information for Business Card
Dr. Bram Holtvick, D.C.
Clinic name - Fernway Chiropractic
2 clinics
location #1
20418 NW Marwick Road
Suite B
North Plains, OR 97133
Location #2
13529 SE Calloway Street
Portland OR 97236
Main phone line 971.555.0143
website : www.FernwayClinics.example
Tag line "Who would you be without pain?"
Colors
Designer to choose colors to be used in the design.
Requirements
Must have
- Use the logo colors -- Want the orange color to be a TRUE orange.
- Both clinic address
- phone number
- website
- personal email - b.holtvick@ReliefBeginsHere.example
- tag line - "Who would you be without pain?"

```html
<!DOCTYPE html>
<html lang="en">
<head>
<meta charset="utf-8">
<title>Fernway Chiropractic – Business Card</title>
<link rel="stylesheet" href="https://fonts.googleapis.com/css2?family=Source+Sans+3:wght@400;600;700&display=swap">
<style>
  :root {
    --orange: #f7941d;
    --charcoal: #333333;
    --ink: #1f1f1f;
    --grey-text: #555555;
    --paper: #ecebe7;
    --backdrop: #d3d3ce;
    --white: #ffffff;
  }
  * { box-sizing: border-box; margin: 0; padding: 0; }
  html, body {
    width: 1200px; height: 801px; overflow: hidden;
    background: var(--backdrop);
    font-family: "Source Sans 3", Arial, sans-serif;
  }
  .stage {
    position: relative; width: 1200px; height: 801px;
  }
  .card {
    position: absolute; top: 252px;
    width: 520px; height: 297px;
    border-radius: 3px;
    box-shadow: 0 3px 0 var(--orange), 0 10px 24px rgba(0,0,0,0.18);
  }
  /* Front side */
  .card--front {
    left: 60px; background: var(--paper);
  }
  .wordmark {
    position: absolute;
    font-weight: 700; text-transform: uppercase;
    letter-spacing: 0.16em; line-height: 1.05;
  }
  .card--front .wordmark {
    left: 34px; bottom: 40px; color: var(--ink);
    font-size: 30px;
  }
  .wordmark small {
    display: block; font-size: 15px; letter-spacing: 0.24em; margin-top: 6px;
  }
  .wordmark-square {
    display: block; width: 22px; height: 22px;
    background: var(--orange); margin-bottom: 14px;
  }
  .details {
    position: absolute; left: 276px; top: 30px; right: 20px;
    color: var(--grey-text); font-size: 12.5px; line-height: 1.3;
  }
  .details__name {
    color: var(--orange); font-weight: 600; font-size: 17px; line-height: 1.2;
  }
  .details__clinic { margin-bottom: 12px; }
  .details__address { margin-bottom: 8px; }
  .details__rule {
    width: 26px; height: 2px; background: var(--orange); margin: 0 0 8px;
  }
  .details__contact { margin-top: 12px; list-style: none; }
  .details__contact li {
    display: flex; align-items: center; gap: 7px; white-space: nowrap;
  }
  .details__contact svg { width: 10px; height: 10px; flex: none; }

  /* Back side */
  .card--back {
    left: 620px; background: var(--charcoal);
    display: flex; flex-direction: column; align-items: center; justify-content: center;
  }
  .card--back .wordmark {
    position: static; color: var(--white); font-size: 34px; text-align: center;
  }
  .card--back .wordmark-square { margin: 0 auto 16px; }
  .tagline {
    color: var(--white); font-size: 17px; margin-top: 34px;
  }
</style>
</head>
<body>
<main class="stage">
  <section class="card card--front" aria-label="Business card front">
    <div class="wordmark">
      <span class="wordmark-square"></span>
      Fernway
      <small>Chiropractic</small>
    </div>
    <div class="details">
      <p class="details__name">Dr. Bram Holtvick, D.C.</p>
      <p class="details__clinic">Clinic name - Fernway Chiropractic</p>
      <p class="details__address">20418 NW Marwick Road<br>Suite B<br>North Plains, OR 97133</p>
      <div class="details__rule"></div>
      <p class="details__address">13529 SE Calloway Street<br>Portland OR 97236</p>
      <ul class="details__contact">
        <li>
          <svg viewBox="0 0 10 10" aria-hidden="true"><path d="M2 0.8 L3.6 2.8 L2.8 3.8 Q3.8 5.8 6 7.2 L7 6.4 L9.2 8 L8.2 9.4 Q3.8 9 0.8 2 Z" fill="var(--orange)"/></svg>
          971.555.0143
        </li>
        <li>
          <svg viewBox="0 0 10 10" aria-hidden="true"><rect x="0.7" y="2" width="8.6" height="6" fill="none" stroke="var(--orange)" stroke-width="1.1"/><path d="M0.8 2.2 L5 5.4 L9.2 2.2" fill="none" stroke="var(--orange)" stroke-width="1.1"/></svg>
          b.holtvick@ReliefBeginsHere.example
        </li>
        <li>
          <svg viewBox="0 0 10 10" aria-hidden="true"><circle cx="5" cy="5" r="4.3" fill="var(--orange)"/><path d="M0.7 5 H9.3 M5 0.7 Q2.6 5 5 9.3 M5 0.7 Q7.4 5 5 9.3" fill="none" stroke="var(--paper)" stroke-width="0.7"/></svg>
          www.FernwayClinics.example
        </li>
      </ul>
    </div>
  </section>

  <section class="card card--back" aria-label="Business card back">
    <div class="wordmark">
      <span class="wordmark-square"></span>
      Fernway
      <small>Chiropractic</small>
    </div>
    <p class="tagline">Who would you be without pain?</p>
  </section>
</main>
</body>
</html>
```